Brochure Design Project

We need a brochure design for our company called Brightwell Motorhomes.
We specialise in converting new or used buses/vans into motorhomes and campervans.

Our brochure will need to have our packages (refer to 'packages' on our website), pictures of conversions we've done previously and a list of our services. It will also need to have that we offer finance.

We would also like to have our logo (attached) and also our contact details, website and email on the brochure.
Our brochure needs to be eye catching as we will be handing it out at events.

Website: www.brightwellmotorhomes-demo.com.au

Please note: website is in the process of being upgraded. Please find attached new logo.

Target Market(s)

Mainly couples between the age of 40-70yrs

Industry/Entity Type

Finance

```html
<!DOCTYPE html>
<html lang="en">
<head>
<meta charset="utf-8">
<title>Brightwell Motorhomes – Services and Packages</title>
<link href="https://fonts.googleapis.com/css2?family=Source+Sans+3:ital,wght@0,400;0,600;0,700;1,700&display=swap" rel="stylesheet">
<style>
:root{
  --page:#d9dadd;
  --panel-mid:#2f74bd;
  --panel-inner:#245fa6;
  --panel-edge:#0f3b78;
  --frame:#ffffff;
  --accent:#f7a823;
  --text:#ffffff;
}
*{margin:0;padding:0;box-sizing:border-box}
html,body{width:1200px;height:932px;overflow:hidden}
body{
  position:relative;
  font-family:"Source Sans 3",Arial,sans-serif;
  color:var(--text);
  background:var(--page);
}
.panel{
  position:absolute;
  border:2px solid var(--frame);
  border-radius:9px;
  box-shadow:0 0 6px rgba(0,0,0,.45);
  background:radial-gradient(ellipse at 50% 45%,var(--panel-mid) 0%,var(--panel-inner) 55%,var(--panel-edge) 100%);
  overflow:hidden;
}
.panel--services{left:15px;top:17px;width:380px;height:899px;padding:0 18px 0 11px}
.panel--packages{left:413px;top:17px;width:771px;height:899px}

.services__title{font-size:23.5px;font-weight:700;text-align:center;line-height:31px;margin:22px 0 12px;text-transform:uppercase}
.service{margin-bottom:14px}
.service__name{color:var(--accent);font-style:italic;font-weight:700;font-size:13.5px;line-height:15px;text-transform:uppercase}
.service__text{font-size:11.8px;line-height:14.6px}

.packages__title{position:absolute;left:0;right:0;top:6px;text-align:center;font-size:26px;font-weight:700;letter-spacing:.5px}
.pkg{position:absolute}
.pkg__name{font-size:25px;font-weight:700;color:var(--accent);white-space:nowrap;line-height:28px}
.pkg__price{color:var(--text)}
.pkg__fit{font-size:11px;line-height:13px;margin-left:4px}
.pkg__intro{position:absolute;text-align:center;font-size:14.5px;line-height:18.2px}
.block-head{color:var(--accent);font-weight:700;font-size:17px;line-height:19px}
.features{position:absolute}
.features li{list-style:none;font-weight:700;font-size:13px;line-height:16.2px;padding-left:2px}
.specs{position:absolute}
.specs li{list-style:none;font-size:11.4px;line-height:14px}
.interior{position:absolute}
.interior li{list-style:none;font-size:11.3px;line-height:14.3px;padding-left:4px}
.interior--tight li{line-height:14px}
.interior li.wrap{padding-left:9px}
</style>
</head>
<body>

<section class="panel panel--services">
  <h1 class="services__title">We offer a wide range of services</h1>

  <div class="service"><h2 class="service__name">» Motorhome conversions</h2>
    <p class="service__text">Whether you are wanting a complete drive away package for the serious traveller including all the little creature comforts to take off around the country or enough to get away from the hussle and bussle for a weekend or anything in between, we do it all. With a huge range of layouts, colours and extras we will be sure to supply you with your desired fitout. Choose from one of our package deals or design your own.</p></div>

  <div class="service"><h2 class="service__name">» Campervan conversions</h2>
    <p class="service__text">We can help you design and completely install any van you have purchased. Choose from one of our package deals or design your own.</p></div>

  <div class="service"><h2 class="service__name">» Goosenecks/Horsefloats</h2>
    <p class="service__text">Instead of paying for a hotel/motel or sleeping in the back of your car, why not utilize your horsefloat into a fully contained motorhome!</p></div>

  <div class="service"><h2 class="service__name">» General upholestry</h2>
    <p class="service__text">Want to change the colours of the walls, roof, curtains or vinyl flooring? Bring in your own upholestry or choose from our range.</p></div>

  <div class="service"><h2 class="service__name">» Additions &amp; alterations</h2>
    <p class="service__text">If their is something missing in your motorhome, campervan or caravan such as an air conditioner, extra water tanks, domestra camper windows, solar power, extra L.E.D lights, roof vents, steps or anything related to motorhomes, we can supply and completely install it for you.</p></div>

  <div class="service"><h2 class="service__name">» Repairs &amp; maintenance</h2>
    <p class="service__text">If something is damaged, falling apart or just need fixing, bring it in for a free quote.</p></div>

  <div class="service"><h2 class="service__name">» Heavy duty drawer runners</h2>
    <p class="service__text">We can supply and install heavy duty full extension drawer system to the boot of 4wd's and motorhomes. With a large weight rating, these make for a very impressive storage area.</p></div>

  <div class="service"><h2 class="service__name">» Boat flooring</h2>
    <p class="service__text">Need a casting deck, extra storage or just a decent solid floor in your boat? All floors are custom made to size then upholstered in the latest high quality marine carpet.</p></div>

  <div class="service"><h2 class="service__name">» Solar power</h2>
    <p class="service__text">Sick of running out of battery power while your meant to be out having a relaxful time. Talk to us about having a maintance free solar power system connected to your motorhome. campervan or caravan.</p></div>

  <div class="service"><h2 class="service__name">» General help</h2>
    <p class="service__text">If you have any questions regarding anything related to motorhomes , feel free to stop by our showroom. Purchasing a motorhome for the first time can be a dawting task, we may be able to help steer you in the right direction.</p></div>
</section>

<section class="panel panel--packages">
  <h1 class="packages__title">OUR&nbsp; PACKAGES</h1>

  <!-- Grande -->
  <div class="pkg" style="left:14px;top:46px">
    <h2 class="pkg__name">Grande - <span class="pkg__price">$29,950.00</span></h2>
    <p class="pkg__fit">- for buses such as Torvan Coachliner, Hiro Arcbus Nexa Citybus etc.</p>
  </div>
  <p class="pkg__intro" style="left:22px;top:101px;width:334px">Our most popular conversion and best value for money! The Grandé is the ultimate conversion when choosing your motorhome. With an innovative and spacious layout, it is designed for those that demand the finest when travelling. Again, the Grande comes with the option of having a double bed or twin single beds. Single bed conversion $29,950.00 Double bed conversion $28,950.00</p>
  <div class="features" style="left:30px;top:252px"><h3 class="block-head">Standard Features</h3>
    <ul><li>-Bathroom</li><li>-Bedroom</li><li>-Lounge Area</li><li>-Kitchen</li></ul></div>
  <div class="specs" style="left:220px;top:252px"><h3 class="block-head">Specifications</h3>
    <ul><li>-Fresh Water:130L</li><li>-Grey Water:50L</li><li>-Hot water Capacity:22L</li></ul></div>
  <div class="interior" style="left:16px;top:343px"><h3 class="block-head">General Interior</h3>
    <ul>
      <li>-2 x Versatile rear lounges/dinette that can be utilized as two single</li>
      <li class="wrap">beds or be folded down to make a double bed</li>
      <li>-Removable table&nbsp; with laminated table top</li>
      <li>-Generous over head storage at rear</li>
      <li>-Tall wardrobe cupboard</li>
      <li>-Metal drawer runners</li>
      <li>-Polished Tasmanian Oak radius bench tops</li>
      <li>-Radius edge gable panels</li>
      <li>-Stainless steel handles on cabinet doors</li>
      <li>-Plywood floor substrate with commercial grade vinyl flooring</li>
      <li>-2 x Fiorra wind up roof hatches</li>
      <li>-Insulated wall and roof lining</li>
    </ul></div>

  <!-- Back to Basics -->
  <div class="pkg" style="left:393px;top:46px">
    <h2 class="pkg__name">Back to Basics - <span class="pkg__price">$19,990.00</span></h2>
  </div>
  <p class="pkg__intro" style="left:398px;top:101px;width:364px">Introducing the all new BACK TO BASICS range for 2012. Want to get on the road sooner but find all the bells and whistles a little unnecessary? Well our BACK TO BASICS range is ideal for you! Suitable for most buses 7mtrs in length.</p>
  <div class="features" style="left:409px;top:252px"><h3 class="block-head">Standard Features</h3>
    <ul><li>-Bedroom</li><li>-Lounge Area</li><li>-Kitchen</li></ul></div>
  <div class="specs" style="left:599px;top:252px"><h3 class="block-head">Specifications</h3>
    <ul><li>-Fresh water: 60ltr</li><li>-Grey water: 50ltr</li></ul></div>
  <div class="interior" style="left:396px;top:343px"><h3 class="block-head">General Interior</h3>
    <ul>
      <li>-New plywood substrate with commercial vinyl flooring throughout</li>
      <li>-Upholstered wall panels</li>
      <li>-12mm Balsa core ply construction</li>
      <li>-Metal drawer runners</li>
      <li>-Laminated square edge bench tops</li>
      <li>-Stainless steel handles on all cupboard doors</li>
      <li>-1 x Fiorra wind up roof hatch</li>
    </ul></div>

  <!-- Freedom -->
  <div class="pkg" style="left:14px;top:549px">
    <h2 class="pkg__name">Freedom - <span class="pkg__price">$42,950.00</span></h2>
    <p class="pkg__fit">-Ideal for larger size vans such as Meridian Strider, Volta Carrier,<br>&nbsp;Ivano Dayliner etc</p>
  </div>
  <div class="features" style="left:30px;top:604px"><h3 class="block-head">Standard Features</h3>
    <ul><li>-Bathroom</li><li>-Bedroom</li><li>-Lounge Area</li><li>-Kitchen</li></ul></div>
  <div class="specs" style="left:220px;top:604px"><h3 class="block-head">Specifications</h3>
    <ul><li>-Fresh water: 100ltr</li><li>-Grey water: 50ltr</li><li>-Hot water capacity: 22ltr</li></ul></div>
  <div class="interior interior--tight" style="left:16px;top:697px"><h3 class="block-head">General Interior</h3>
    <ul>
      <li>-2 x Versatile rear lounges/dinette that can be utilized as two single beds</li>
      <li class="wrap">or be folded down to make a double bed</li>
      <li>-Removable table with lamonated table top</li>
      <li>-Generous over head storage at rear</li>
      <li>-Tall wardrobe cupboard</li>
      <li>-Metal drawer runners</li>
      <li>-Polished Tasmanian Oak radius bench tops</li>
      <li>-Radius edge gable panels</li>
      <li>-Stainless steel handles on cabinet doors</li>
      <li>-Plywood floor substrate with commercial grade vinyl flooring</li>
      <li>-2 x Fiorra wind up roof hatches</li>
      <li>-Insulated wall and roof lining</li>
    </ul></div>

  <!-- Easy Getaway -->
  <div class="pkg" style="left:393px;top:549px">
    <h2 class="pkg__name">Easy Getaway - <span class="pkg__price">$21,490.00</span></h2>
    <p class="pkg__fit">-Ideal for small vans such as Torvan Hivan, Meridian MV, etc</p>
  </div>
  <div class="features" style="left:409px;top:604px"><h3 class="block-head">Standard Features</h3>
    <ul><li>-Kitchen</li><li>-Bedroom / Dining area</li></ul></div>
  <div class="specs" style="left:599px;top:604px"><h3 class="block-head">Specifications</h3>
    <ul><li>-Freshwater: 20ltr</li><li>-Grey water: 10ltr</li></ul></div>
  <div class="interior interior--tight" style="left:396px;top:697px"><h3 class="block-head">General Interior</h3>
    <ul>
      <li>-1 x Fiorra wind up roof hatch</li>
      <li>-New plywood floor substrate with commercial grade vinyl flooring</li>
      <li class="wrap">throughout</li>
      <li>-New insulated wall and roof lining</li>
    </ul></div>
</section>

</body>
</html>
```